2in1 Bartender & Sommelier needs a business card

I need a business card. I worked as a bartender in many places but I just finished a sommelier school and I would like a new business card. I like minimal design, natural materials and something what makes the people think :) I try to be creative in cocktail making, like little mixology, little twist on recipes... I like to travel and discover new places, cultures and of course interesting drinks and improve continously...live a little bit crazy life. And I like what I do...

Target Market(s)

restaurant/winebar managers, winemakers, other sommeliers and bartenders, people who work in food and beverage sector

Industry/Entity Type

Hospitality

Contact Information for Business Card

Réka Fodor
Bartender & Sommelier
Phone: (FR) +33 6 4720 3917
(HU) +36 70 518 6092

Font styles to use
Script

Requirements
Must have
• Some sign, I am a bartender and sommelier as well.
Nice to have
• black and white maybe with 1 or 2 extra color
Should not have
• very colourful, to many things on the card

```html
<!DOCTYPE html>
<html lang="en">
<head>
<meta charset="utf-8">
<title>Réka Fodor — Business Card</title>
<link rel="stylesheet" href="https://fonts.googleapis.com/css2?family=Roboto:wght@400;700&family=Pinyon+Script&display=swap">
<style>
  :root {
    --navy: #1d3566;
    --navy-deep: #142a55;
    --navy-light: #26447c;
    --paper: #f7f7f6;
    --paper-shade: #e9e9e8;
    --ink: #2b2b2b;
    --rule: #3a3a3a;
    --gold: #c98a2e;
    --gold-deep: #a9651c;
    --backdrop: #dcdad6;
    --ghost: rgba(0, 0, 0, 0.06);
  }
  * { box-sizing: border-box; margin: 0; padding: 0; }
  html, body {
    width: 1200px;
    height: 780px;
    overflow: hidden;
    background: var(--backdrop);
  }
  .canvas {
    width: 1200px;
    height: 780px;
    display: flex;
    align-items: center;
    justify-content: center;
    gap: 60px;
  }
  .card {
    position: relative;
    width: 525px;
    height: 300px;
    overflow: hidden;
    box-shadow: 0 6px 18px rgba(0, 0, 0, 0.18);
  }

  /* Front side */
  .card--front {
    background: linear-gradient(135deg, var(--paper) 0%, var(--paper-shade) 100%);
  }
  .front__ghost-name {
    position: absolute;
    top: 18px;
    left: 40px;
    font-family: "Roboto", sans-serif;
    font-weight: 400;
    font-size: 84px;
    color: var(--ghost);
    white-space: nowrap;
  }
  .front__band {
    position: absolute;
    left: 0;
    right: 0;
    bottom: 0;
    height: 74px;
    background: linear-gradient(90deg, var(--navy-deep), var(--navy-light));
  }
  .front__band-edge {
    position: absolute;
    left: 0;
    right: 0;
    bottom: 80px;
    height: 1px;
    background: var(--rule);
    opacity: 0.5;
  }
  .front__seal {
    position: absolute;
    left: 34px;
    bottom: 36px;
    width: 78px;
    height: 78px;
    border-radius: 50%;
    background: radial-gradient(circle at 35% 35%, var(--gold), var(--gold-deep));
    border: 4px solid #fff;
  }
  .front__details {
    position: absolute;
    left: 150px;
    top: 112px;
    font-family: "Roboto", sans-serif;
    color: var(--ink);
  }
  .front__name {
    font-weight: 700;
    font-size: 24px;
    color: var(--navy);
    line-height: 1.1;
  }
  .front__title {
    font-size: 15px;
    margin-top: 2px;
  }
  .front__rule {
    width: 340px;
    height: 1px;
    background: var(--rule);
    margin: 10px 0 8px;
  }
  .front__phones {
    list-style: none;
    font-size: 15px;
    line-height: 1.35;
  }
  .front__country {
    color: var(--navy);
    margin-right: 4px;
  }

  /* Back side */
  .card--back {
    background: linear-gradient(160deg, var(--navy-light) 0%, var(--navy) 55%, var(--navy-deep) 100%);
    display: flex;
    align-items: center;
    justify-content: center;
    gap: 22px;
  }
  .back__name {
    font-family: "Pinyon Script", cursive;
    font-size: 58px;
    color: #fff;
    white-space: nowrap;
  }
  .back__seal {
    width: 74px;
    height: 74px;
    border-radius: 50%;
    background: radial-gradient(circle at 35% 35%, var(--gold), var(--gold-deep));
    flex: none;
  }
</style>
</head>
<body>
  <main class="canvas">
    <section class="card card--front" aria-label="Card front">
      <div class="front__ghost-name" aria-hidden="true">Réka Fodor</div>
      <div class="front__band-edge"></div>
      <div class="front__band"></div>
      <div class="front__seal"></div>
      <div class="front__details">
        <h1 class="front__name">Réka Fodor</h1>
        <p class="front__title">Bartender &amp; Sommelier</p>
        <div class="front__rule"></div>
        <ul class="front__phones">
          <li><span class="front__country">(FR)</span>+33 6 4720 3917</li>
          <li><span class="front__country">(HU)</span>+36 70 518 6092</li>
        </ul>
      </div>
    </section>

    <section class="card card--back" aria-label="Card back">
      <p class="back__name">Réka Fodor</p>
      <div class="back__seal"></div>
    </section>
  </main>
</body>
</html>
```